Signal Post Hire Banner Ad Design Project

Hello Sketch Guild,

We are looking for a banner ad that we can email to general contractors, and consulting firms in our service area to make them aware of our service.

We are an electrical contracting company based in Toronto, Ontario, Canada and one of divisions rents traffic light systems. We install our portable systems mainly in underground parking garages when construction restricts two way traffic to one lane. Our systems also get installed on ramps, and other areas that are under construction. Essentially, they allow phasing of big construction projects so the disruptions of traffic flow is kept to a minimal.
Our systems differ from other companies' rentals because our systems are cheaper, more reliable since they aren't wireless and they are LED (no bulbs burning out), we provide countdown lights that increase the effectiveness of the system and motorists' patience, and our systems adapt to rush hour traffic flow patterns at each site.
We have installed the systems at high profile locations throughout the city including The Halvern Marbury Plaza, and Quillmont Mall.
We can provide job specific pricing or a monthly rate both of which include installation and removal.

I don't have very many good images of our systems but maybe you can photoshop our systems into another photo or a stock image might work as well.

More information on our systems can be found at www.brantwickpower.example
Updates

Project Deadline Extended
Reason: Hi everyone, I am extending the deadline for submissions because I haven't had a proper chance to provide feedback to some of the designers who have submitted banner ads. I know it is frustrating when the deadline gets extended and I apologize. Thank you again and if I haven't provided feedback to you yet, please be patient because there have been some excellent designs that have been submitted so far. Dale

Project Deadline Extended
Reason: Still working with designers towards the right design.

Project Deadline Extended
Reason: I have been swamped with work and haven't been able to provide proper feedback to designers. Thanks for your patience, Dale

Industry/Entity Type

Construction

Requirements
Must have
• Brantwick Power Logo

Focus on the fact that our systems are lower in price than our competitors or the fact that they are more cost effective.

Something that touches on the fact that our systems have countdown lights and adaptive control which increases traffic flow. This is a unique feature that no other company has.

```html
<!DOCTYPE html>
<html lang="en">
<head>
<meta charset="utf-8">
<title>Signal Post Hire – Banner</title>
<link rel="stylesheet" href="https://fonts.googleapis.com/css2?family=Cabin:wght@400;500;600;700&display=swap">
<style>
  :root {
    --ink-dark: #2a2622;
    --header-bg: rgba(38, 33, 30, 0.94);
    --orange: rgba(240, 148, 30, 0.93);
    --pale: rgba(236, 236, 234, 0.9);
    --text-brown: #3a2a1c;
    --white: #ffffff;
    --logo-grey: #6d6e70;
    --partner-red: #d7262e;
  }
  * { margin: 0; padding: 0; box-sizing: border-box; }
  html, body { width: 1200px; height: 898px; overflow: hidden; background: #fff; }
  body { font-family: "Cabin", "Trebuchet MS", sans-serif; }

  .banner {
    position: relative;
    width: 1200px;
    height: 898px;
    overflow: hidden;
    border: 3px solid #d8d8d8;
  }
  .site-photo {
    position: absolute;
    inset: 0;
    background:
      radial-gradient(circle at 845px 230px, rgba(255,240,200,0.95) 0, rgba(240,110,60,0.85) 90px, rgba(120,40,30,0.35) 200px, rgba(0,0,0,0) 320px),
      radial-gradient(circle at 1070px 820px, rgba(220,60,50,0.7) 0, rgba(0,0,0,0) 110px),
      linear-gradient(135deg, #6b6460 0%, #4a4440 40%, #3a3532 70%, #57514d 100%);
  }

  .info-panel {
    position: absolute;
    left: 0;
    top: 43px;
    width: 625px;
  }
  .panel-title {
    height: 131px;
    background: var(--header-bg);
    color: var(--white);
    font-weight: 500;
    font-size: 47px;
    letter-spacing: 1px;
    display: flex;
    align-items: center;
    padding-left: 36px;
  }
  .feature-list {
    height: 288px;
    background: var(--orange);
    list-style: none;
    padding: 36px 0 0 72px;
  }
  .feature {
    display: flex;
    align-items: center;
    height: 76px;
    font-size: 41px;
    color: var(--text-brown);
  }
  .feature svg { width: 42px; height: 42px; margin-right: 26px; flex: none; }

  .brand-strip {
    position: relative;
    height: 293px;
    background: var(--pale);
    overflow: hidden;
  }
  .client-name {
    position: absolute;
    left: 36px;
    top: 60px;
    display: flex;
    flex-direction: column;
    align-items: flex-start;
    gap: 16px;
  }
  .client-mark {
    width: 80px;
    height: 80px;
    background: var(--logo-grey);
  }
  .client-name span {
    font-size: 40px;
    font-weight: 600;
    color: var(--logo-grey);
    line-height: 1.05;
    width: 200px;
  }
  .association {
    position: absolute;
    left: 273px;
    top: 78px;
    font-size: 18px;
    font-weight: 700;
    letter-spacing: 3.4px;
    color: var(--ink-dark);
  }
  .partner-name {
    position: absolute;
    left: 258px;
    top: 128px;
    display: flex;
    align-items: center;
    gap: 14px;
  }
  .partner-mark {
    width: 96px;
    height: 96px;
    border-radius: 50%;
    background: var(--partner-red);
    flex: none;
  }
  .partner-name span {
    font-size: 33px;
    font-weight: 600;
    color: var(--ink-dark);
    line-height: 1.1;
    white-space: nowrap;
  }
</style>
</head>
<body>
<div class="banner">
  <div class="site-photo" role="img" aria-label="Photo of a lit red portable traffic signal in an underground parking garage, with a red countdown display below"></div>

  <section class="info-panel">
    <h1 class="panel-title">SIGNAL POST HIRE</h1>
    <ul class="feature-list">
      <li class="feature">
        <svg viewBox="0 0 24 24" aria-hidden="true">
          <path d="M3 12 L12 3 L21 3 L21 12 L12 21 Z" fill="#fff" stroke="#3a2a1c" stroke-width="1.5" stroke-linejoin="round"/>
          <circle cx="17" cy="7" r="1.6" fill="#3a2a1c"/>
        </svg>
        Cost Effective
      </li>
      <li class="feature">
        <svg viewBox="0 0 24 24" aria-hidden="true">
          <rect x="2" y="4" width="20" height="16" rx="1.5" fill="#2a2622"/>
          <text x="12" y="16.5" text-anchor="middle" font-family="Cabin, sans-serif" font-size="11" font-weight="700" fill="#fff">10</text>
        </svg>
        Countdown Lights
      </li>
      <li class="feature">
        <svg viewBox="0 0 24 24" aria-hidden="true">
          <circle cx="12" cy="13" r="9" fill="#2a2622"/>
          <circle cx="12" cy="13" r="4.5" fill="none" stroke="#fff" stroke-width="2"/>
          <rect x="10.5" y="1.5" width="3" height="3" fill="#2a2622"/>
        </svg>
        Adaptive cControl
      </li>
    </ul>
    <div class="brand-strip">
      <div class="client-name">
        <div class="client-mark"></div>
        <span>Brantwick Power</span>
      </div>
      <p class="association">IN ASSOCIATION WITH</p>
      <div class="partner-name">
        <div class="partner-mark"></div>
        <span>signalposthire<br>.example</span>
      </div>
    </div>
  </section>
</div>
</body>
</html>
```